依頼詳細
新規開院に併せて内覧会を開催いたします。
その告知用に折込チラシの配布・ポスティング配布を実施します。
地域の皆様に開院を広く知っていただけるようなシンプルかつインパクトのある、わかりやすいチラシデザインをお願いいたします。ベースのカラーはピンク系が希望です。
女性・高齢者の方に院を知っていただき、アピールできるようなデザインをお願いいたします。
記載項目
・院名/住所/電話番号/施術受付時間/地図/院長よりメッセージなど。
・内覧会開催のお知らせ、開催日(変更になる可能性があります)
・オープンに先がけて内覧会を開催します。
・実際のオープン日など(変更になる可能性があります)
サイズ
A4
ページ数
片面
希望イメージ
シンプル 複雑
単色 カラフル
暗い 明るい
日常 高級
遊び心 厳粛
未来的 伝統的
女性的 男性的
希望する色
赤系、ピンクを中心にお願いいたします。
納品ファイル
• 高解像度JPG (.jpg)
• イラストレーター形式 (.ai)
補足説明
新規開業の接骨院の為、地域の皆様に認知していただけるような親しみがあり、インパクトのあるチラシデザインをお願いいたします。

シンプルでわかりやすいイメージが気に入りました。
地域の皆様に愛される接骨院のイメージが沸きましたので、このデザインに決定いたしました。

たくさんのご提案ありがとうございました。
決定までお時間をいただき申し訳ありませんでしたが、
最初の直感で決定いたしました。またの機会がございましたら
ご提案宜しくお願いいたします。

```html
<!DOCTYPE html>
<html lang="ja">
<head>
<meta charset="utf-8">
<title>さくらぎ接骨院 内覧会開催のご案内</title>
<link href="https://fonts.googleapis.com/css2?family=M+PLUS+Rounded+1c:wght@400;700;800;900&display=swap" rel="stylesheet">
<style>
  :root {
    --pink: #ef7a95;
    --pink-deep: #e2587a;
    --pink-pale: #fde6ec;
    --yellow: #fff3b0;
    --gold: #f5c000;
    --orange: #f39800;
    --white: #ffffff;
    --ink: #4a3a3a;
    --grey: #8a7f80;
  }
  * { margin: 0; padding: 0; box-sizing: border-box; }
  html, body { width: 846px; height: 1200px; overflow: hidden; }
  body {
    font-family: "M PLUS Rounded 1c", sans-serif;
    background: var(--pink);
    color: var(--ink);
    position: relative;
  }
  .flyer { position: absolute; inset: 0; }

  .open-badge {
    position: absolute; left: 22px; top: 18px;
    width: 130px; padding: 10px 8px;
    background: var(--white); color: var(--pink-deep);
    font-weight: 900; font-size: 26px; line-height: 1.25; text-align: center;
    border-radius: 6px;
  }
  .promise {
    position: absolute; left: 200px; top: 22px; width: 610px; height: 98px;
    background: var(--yellow); border-radius: 20px;
    display: flex; flex-direction: column; justify-content: center; align-items: center;
    color: var(--pink-deep); font-weight: 800; font-size: 30px; line-height: 1.35;
  }
  .promise::after {
    content: ""; position: absolute; bottom: -16px; left: 50%; margin-left: -14px;
    border: 14px solid transparent; border-top: 16px solid var(--yellow); border-bottom: 0;
  }

  .headline {
    position: absolute; left: 22px; right: 22px; top: 140px; height: 200px;
    background: var(--pink-pale); border-radius: 12px; text-align: center;
  }
  .clinic-title {
    margin-top: 10px; font-size: 74px; font-weight: 900; color: var(--pink-deep); letter-spacing: 2px;
  }
  .event-title {
    font-size: 56px; font-weight: 900; color: var(--pink); letter-spacing: 2px; margin-top: -8px;
  }
  .event-title small { font-size: 40px; }

  .event-date {
    position: absolute; left: 0; right: 0; top: 340px; text-align: center;
    display: flex; justify-content: center; align-items: flex-end; gap: 14px;
  }
  .event-date .day { font-size: 76px; font-weight: 900; color: var(--gold); line-height: 1; }
  .event-date .day span {
    display: inline-block; font-size: 30px; width: 40px; height: 40px; line-height: 40px;
    background: var(--gold); color: var(--white); border-radius: 50%; vertical-align: middle;
  }
  .event-date .time { color: var(--white); font-size: 16px; text-align: left; line-height: 1.5; padding-bottom: 8px; }

  .treatment-art {
    position: absolute; left: 260px; right: 22px; top: 440px; height: 370px;
    border-radius: 16px;
    background: linear-gradient(160deg, #f6d2b4 0%, #a9d7ea 55%, #6fb7d8 100%);
  }

  .symptoms {
    position: absolute; left: 20px; top: 470px; width: 300px; height: 300px;
    border-radius: 50%; background: var(--yellow);
    display: flex; flex-direction: column; justify-content: center; align-items: center;
    text-align: center; color: var(--pink-deep);
  }
  .symptoms h2 { font-size: 21px; font-weight: 800; line-height: 1.3; margin-bottom: 8px; }
  .symptoms ul { list-style: none; font-size: 16px; font-weight: 700; color: var(--ink); line-height: 1.5; }

  .open-day {
    position: absolute; left: 22px; top: 820px;
    background: var(--white); color: var(--orange);
    font-size: 36px; font-weight: 900; padding: 6px 16px; border-radius: 6px; line-height: 1.3;
  }

  .info-panel {
    position: absolute; left: 22px; right: 22px; top: 930px; bottom: 22px;
    background: var(--white); border-radius: 10px;
  }
  .clinic-info { position: absolute; left: 24px; top: 20px; width: 360px; }
  .clinic-name { font-size: 36px; font-weight: 800; color: var(--grey); }
  .address { font-size: 13px; color: var(--grey); margin-top: 4px; }
  .phone {
    display: flex; align-items: center; gap: 8px; margin-top: 8px;
    font-size: 40px; font-weight: 900; color: var(--pink-deep); letter-spacing: 1px;
  }
  .phone svg { width: 32px; height: 32px; }
  .hours { font-size: 13px; color: var(--grey); margin-top: 6px; line-height: 1.6; }

  .director-message {
    position: absolute; left: 380px; top: 16px; width: 150px; height: 210px;
    border-radius: 75px; background: var(--pink-pale);
    padding: 22px 14px; font-size: 11px; line-height: 1.6; color: var(--ink);
  }
  .director-message h3 {
    font-size: 13px; color: var(--white); background: var(--pink); border-radius: 10px;
    text-align: center; margin-bottom: 6px;
  }
  .area-map {
    position: absolute; right: 18px; top: 16px; width: 240px; height: 214px;
    background: linear-gradient(135deg, #f1ecec, #dcd5d6); border: 1px solid #d3c9ca;
  }
</style>
</head>
<body>
<main class="flyer">
  <div class="open-badge">花岡市に<br>新規開院</div>
  <div class="promise"><p>患者様1人1人に寄り添い</p><p>痛みの根本から治療します。</p></div>

  <section class="headline">
    <h1 class="clinic-title">さくらぎ接骨院</h1>
    <p class="event-title">内覧会開催<small>のご案内</small></p>
  </section>

  <div class="event-date">
    <p class="day">00/00<span>日</span></p>
    <p class="time">［開催時間］<br>00:00〜00:00</p>
  </div>

  <div class="treatment-art" role="img" aria-label="施術者が寝ている患者の背中をほぐすイラスト"></div>

  <aside class="symptoms">
    <h2>このような症状で<br>お悩みの方</h2>
    <ul>
      <li>肩や腰の痛み・</li>
      <li>首や膝の痛み・関節の痛み・</li>
      <li>ねんざ・打撲・挫傷・骨折</li>
      <li>・脱臼・交通事故による</li>
      <li>ケガなど</li>
    </ul>
  </aside>

  <p class="open-day">オープン日は<br>0/0日です。</p>

  <section class="info-panel">
    <div class="clinic-info">
      <p class="clinic-name">さくらぎ接骨院</p>
      <p class="address">〒000-0000　花岡市桜木町0丁目00番地</p>
      <p class="phone">
        <svg viewBox="0 0 32 32" aria-hidden="true"><rect width="32" height="32" rx="5" fill="var(--pink-deep)"/><path d="M11 7c1 0 2 3 2 4s-2 2-2 3 3 5 5 6 2-2 3-2 4 1 4 2-2 4-4 4C13 24 8 17 8 11c0-2 2-4 3-4z" fill="#fff"/></svg>
        0000-000-000
      </p>
      <p class="hours">施術受付時間　月〜土 00:00〜00:00<br>休　診　日　日曜・祝日</p>
    </div>
    <div class="director-message">
      <h3>院長より</h3>
      <p>地域の皆様の健康を支える身近な接骨院を目指します。お体の不調はお気軽にご相談ください。</p>
    </div>
    <div class="area-map" role="img" aria-label="さくらぎ接骨院周辺の地図"></div>
  </section>
</main>
</body>
</html>
```